The Ember Lantern

Look for someone who can add some splash and make this powerpoint presentation more dynamic. Feel free to use color, animations etc to provide some punch.

```html
<!DOCTYPE html>
<html lang="en">
<head>
<meta charset="utf-8">
<title>The Ember Lantern — Module One Deck</title>
<link href="https://fonts.googleapis.com/css2?family=Montserrat:wght@400;500;600;800&family=Roboto+Condensed:wght@300;400;700&family=Open+Sans:wght@400;600;700&display=swap" rel="stylesheet">
<style>
:root{
  --bg:#e4e4e4;
  --ink:#1d1d1d;
  --paper:#ffffff;
  --muted:#4a4a4a;
  --soft:#8a8a8a;
  --mapgrey:#eeeeee;
}
*{margin:0;padding:0;box-sizing:border-box}
html,body{width:1200px;height:935px;overflow:hidden;background:var(--bg)}
body{position:relative;font-family:"Open Sans",Arial,sans-serif;color:var(--ink)}
.slide{position:absolute;width:365px;height:205px;background:var(--paper);overflow:hidden;box-shadow:0 3px 8px rgba(0,0,0,.25)}
.slide > *{position:absolute}
.c1{left:43px}.c2{left:418px}.c3{left:792px}
.r1{top:37px}.r2{top:253px}.r3{top:469px}.r4{top:685px}
.num{right:8px;bottom:8px;font-size:4.5px;color:var(--muted)}
.brand{right:10px;top:10px;display:flex;flex-direction:column;align-items:center;gap:2px;font-family:"Montserrat",sans-serif;font-size:3.3px;letter-spacing:1px;font-weight:500;color:var(--ink)}
.brand::before{content:"";width:6px;height:6px;border-radius:50%;background:currentColor}
.brand.light{color:var(--paper)}
.photo{background:linear-gradient(160deg,#cfcfcf,#8d8d8d 55%,#5c5c5c)}
.dark-img{background:linear-gradient(170deg,#3a3a3a,#141414)}
ul{list-style:none}
ul li{position:relative;padding-left:9px}
ul li::before{content:"•";position:absolute;left:0}
.cond{font-family:"Roboto Condensed",sans-serif}
.mont{font-family:"Montserrat",sans-serif}

/* Slide 1 cover */
.cover{background:var(--ink)}
.cover .bg{inset:0;background:linear-gradient(180deg,#3b3b3b,#1b1b1b 70%,#262626)}
.cover .mark{left:175px;top:72px;width:16px;height:16px;border-radius:50%;background:var(--paper)}
.cover .name{left:0;right:0;top:106px;text-align:center;color:var(--paper);font-family:"Montserrat",sans-serif;font-size:10.5px;letter-spacing:3px;font-weight:500}
.cover .title{left:0;right:0;top:138px;text-align:center;color:var(--paper);font-family:"Montserrat",sans-serif;font-size:19px;font-weight:500}
.cover .rule{left:0;right:0;top:176px;height:1px;background:var(--paper)}
.cover .tag{left:100px;top:171px;width:166px;height:10px;border-radius:5px;background:var(--paper);font-size:6.3px;line-height:10px;text-align:center;font-family:Arial,sans-serif}

/* Slide 2 roadmap */
.map{left:100px;top:48px;width:230px;height:140px;background:radial-gradient(ellipse at center,var(--mapgrey),rgba(255,255,255,0) 70%)}
.s2title{left:16px;top:9px;font-family:"Montserrat",sans-serif;font-weight:600;font-size:11px;line-height:13.5px}
.s2bar{left:16px;top:38px;width:39px;height:2.5px;background:var(--ink)}
.road{left:0;top:0;width:365px;height:205px}
.stop{font-size:5px;line-height:5.3px;color:var(--muted)}
.stop li{margin-bottom:4.5px}
.stop li::before{font-size:5px}

/* Slide 3 */
.s3city{left:142px;top:0;width:223px;height:205px;background:linear-gradient(180deg,#d9d9d9,#8b8b8b 45%,#4a4a4a)}
.s3sq{left:12px;top:8px;width:9px;height:9px;background:var(--ink)}
.s3mod{left:26px;top:72px;font-family:"Montserrat",sans-serif;font-size:14px}
.s3band{left:22px;top:91px;width:185px;height:28px;background:var(--ink)}
.s3t1{left:26px;top:92px;color:var(--paper);font-family:"Roboto Condensed",sans-serif;font-weight:700;font-size:21px;letter-spacing:.3px}
.s3t2{left:26px;top:118px;font-family:"Roboto Condensed",sans-serif;font-weight:700;font-size:21px;display:flex;align-items:center;gap:4px}
.s3t2::after{content:"";width:28px;height:1.5px;background:var(--ink)}

/* Slide 4 about */
.blk{background:var(--ink)}
.s4h1{left:148px;top:52px;font-family:"Montserrat",sans-serif;font-size:12px;font-weight:500}
.s4h2{left:148px;top:64px;font-family:"Montserrat",sans-serif;font-size:20px;font-weight:800}
.s4list{left:160px;top:92px;width:175px;font-family:Arial,sans-serif;font-size:5.4px;line-height:5.8px;color:var(--muted)}
.s4list li{margin-bottom:1.5px;padding-left:7px}

/* Slide 5 results */
.s5h{left:22px;top:17px;color:var(--paper);font-family:"Montserrat",sans-serif;font-weight:800;font-size:24px}
.s5list{left:30px;top:75px;width:175px;font-size:8.3px;line-height:13px;color:var(--muted)}
.s5list li::before{color:var(--ink);font-size:10px}

/* Slide 6 why */
.s6h{left:14px;top:6px;font-family:"Roboto Condensed",sans-serif;font-weight:700;font-size:17px}
.s6u{left:14px;top:29px;width:20px;height:2px;background:var(--ink)}
.s6sub{left:25px;top:52px;font-weight:600;font-size:8.3px}
.s6list{left:25px;top:70px;width:325px;font-size:7px;line-height:10px;color:var(--muted)}

/* Slide 7 results for founders */
.s7img{left:23px;top:22px;width:122px;height:161px}
.s7sq{left:30px;top:30px;width:6px;height:6px;background:var(--paper)}
.s7h{left:37px;top:62px;color:var(--paper);font-family:"Roboto Condensed",sans-serif;font-weight:700;font-size:18px;line-height:23.5px}
.s7list{left:161px;top:27px;width:165px;font-size:7.8px;line-height:11px;color:var(--muted)}

/* Slide 8 who */
.s8img{left:23px;top:22px;width:162px;height:161px}
.s8h{left:33px;top:30px;color:var(--paper);font-family:"Roboto Condensed",sans-serif;font-weight:700;font-size:15.5px;line-height:18px}
.s8u{left:33px;top:71px;width:22px;height:1.5px;background:var(--paper)}
.s8list{left:33px;top:82px;width:145px;color:var(--paper);font-family:Arial,sans-serif;font-size:5.2px;line-height:6px}
.s8list li{margin-bottom:6.5px}
.s8h2{left:198px;top:40px;font-family:"Roboto Condensed",sans-serif;font-size:16px;line-height:19px;font-weight:300}
.s8h2 b{font-weight:700}
.s8line{display:inline-block;width:28px;height:1.5px;background:var(--ink);vertical-align:middle;margin-left:2px}
.s8list2{left:205px;top:108px;width:110px;font-family:Arial,sans-serif;font-size:5.8px;line-height:6.2px;color:var(--muted)}
.s8list2 li{margin-bottom:6px}

/* Slide 9 journey */
.s9h{left:14px;top:14px;font-family:"Roboto Condensed",sans-serif;font-weight:700;font-size:16.5px;line-height:18px}
.s9line{display:inline-block;width:88px;height:1px;background:var(--ink);vertical-align:middle;margin-left:4px}
.vbar{width:19px;height:94px;background:var(--ink);color:var(--paper);font-family:"Roboto Condensed",sans-serif;font-weight:700;font-size:6.5px;display:flex;align-items:center;justify-content:center}
.vbar span{transform:rotate(-90deg);white-space:nowrap}
.s9list{font-size:6px;line-height:6.5px;color:var(--muted);width:110px}
.s9list li{margin-bottom:6.6px;padding-left:7px}
.s9plain li{padding-left:0}
.s9plain li::before{content:none}

/* Slide 10 story */
.s10h{left:14px;top:16px;font-family:"Roboto Condensed",sans-serif;font-weight:700;font-size:14px;line-height:16px}
.s10line{display:inline-block;width:42px;height:1px;background:var(--ink);vertical-align:middle;margin-left:3px}
.s10box{left:0;top:65px;width:182px;height:105px;background:var(--ink)}
.s10list{left:38px;top:74px;width:135px;color:var(--paper);font-size:7px;line-height:11.2px}
.s10list2{left:193px;top:72px;width:150px;font-size:7px;line-height:11.2px;color:var(--muted)}

/* Slide 11 accelerators */
.s11h{left:14px;top:13px;font-family:"Roboto Condensed",sans-serif;font-weight:700;font-size:15px;line-height:17px}
.s11bar{width:18px;height:94px}
.s11list{font-size:6px;line-height:6.3px;color:var(--muted);width:115px}
.s11list li{margin-bottom:4.8px;padding-left:6px}
.s11foot{left:0;right:0;top:166px;text-align:center;font-size:7.3px;line-height:8.5px;color:var(--muted)}

/* Slide 12 road */
.s12img{left:21px;top:21px;width:114px;height:164px}
.s12h{left:38px;top:50px;color:var(--paper);font-family:"Roboto Condensed",sans-serif;font-weight:700;font-size:19px;line-height:24px}
.s12list{left:150px;top:36px;width:200px;font-size:7.2px;line-height:10.3px;color:var(--muted)}
.s12list ul li{padding-left:7px}
</style>
</head>
<body>

<!-- Row 1 -->
<section class="slide cover c1 r1">
  <div class="bg" role="img" aria-label="Black and white aerial city skyline photograph"></div>
  <div class="mark"></div>
  <div class="name">LANTERN PEAK</div>
  <h1 class="title">The Ember Lantern</h1>
  <div class="rule"></div>
  <div class="tag">How to raise faster, get back to building and grow</div>
</section>

<section class="slide c2 r1">
  <div class="map" role="img" aria-label="Faint world map behind the module roadmap"></div>
  <h2 class="s2title">Module One<br>The Fundraising Journey</h2>
  <div class="s2bar"></div>
  <div class="brand">LANTERN PEAK</div>
  <svg class="road" viewBox="0 0 365 205" fill="none" stroke="#1d1d1d" stroke-width="3">
    <path d="M124 88 V66 a6 6 0 0 0 -6 -6 H56 a6 6 0 0 0 -6 6 V165 a6 6 0 0 0 6 6 H118 a6 6 0 0 0 6 -6 V135 L149 93 V66 a6 6 0 0 1 6 -6 H217 a6 6 0 0 1 6 6 V88"/>
    <path d="M149 141 V165 a6 6 0 0 0 6 6 H217 a6 6 0 0 0 6 -6 V135 L248 93 V66 a6 6 0 0 1 6 -6 H316 a6 6 0 0 1 6 6 V165 a6 6 0 0 1 -6 6 H254 a6 6 0 0 1 -6 -6 V141"/>
    <g fill="#1d1d1d" stroke="none">
      <circle cx="124" cy="89" r="4"/><circle cx="149" cy="140" r="4"/>
      <circle cx="223" cy="89" r="4"/><circle cx="248" cy="140" r="4"/>
    </g>
  </svg>
  <ul class="stop" style="left:62px;top:91px;width:55px">
    <li>Welcome</li><li>About Me &amp; My Background</li><li>Why I created this course</li><li>The Fundraising Journey</li>
  </ul>
  <ul class="stop" style="left:161px;top:79px;width:52px">
    <li>It's All About The Story</li><li>Accelerators (Good/Bad/Maybe)</li><li>Why Not Elm Ridge Road?</li><li>The different types of capital</li>
  </ul>
  <ul class="stop" style="left:260px;top:75px;width:52px">
    <li>Where to find the accredited investors?</li><li>Unlocking the Power of Angel Investors</li><li>Early-Stage Fundraising Traps</li><li>The Easiest Money You Will Ever Raise</li>
  </ul>
  <div class="num">2</div>
</section>

<section class="slide c3 r1">
  <div class="s3city" role="img" aria-label="Black and white downtown skyscrapers photograph"></div>
  <div class="s3sq"></div>
  <div class="s3mod">Module One</div>
  <div class="s3band"></div>
  <div class="s3t1">The Fundraising</div>
  <div class="s3t2">Journey</div>
  <div class="brand">LANTERN PEAK</div>
</section>

<!-- Row 2 -->
<section class="slide c1 r2">
  <div class="blk" style="left:0;top:0;width:85px;height:29px"></div>
  <div class="blk" style="left:0;top:29px;width:24px;height:140px"></div>
  <div class="blk" style="left:64px;top:179px;width:85px;height:26px"></div>
  <div class="blk" style="left:139px;top:151px;width:10px;height:30px"></div>
  <div class="photo" style="left:33px;top:41px;width:96px;height:127px" role="img" aria-label="Portrait photograph of the course author"></div>
  <div class="s4h1">About Me &amp; My</div>
  <div class="s4h2">Background</div>
  <ul class="s4list">
    <li>Over the last 25yrs, I helped two companies build business units to revenues over $1B annually.</li>
    <li>Then, in 2018, I burned out.</li>
    <li>So, I decided to leave the corporate executive grind to help early-stage founders.</li>
    <li>So, I started building my company and brand in 2018.</li>
    <li>Since that day, I've spent my time finding ways to help early-stage Founders win!</li>
  </ul>
  <div class="brand">LANTERN PEAK</div>
  <div class="num">4</div>
</section>

<section class="slide c2 r2">
  <div class="blk" style="left:0;top:0;width:270px;height:31px"></div>
  <div class="blk" style="left:0;top:31px;width:207px;height:32px"></div>
  <div class="blk" style="left:251px;top:179px;width:114px;height:26px"></div>
  <div class="blk" style="left:325px;top:151px;width:40px;height:30px"></div>
  <div class="s5h">My Results</div>
  <div class="photo" style="left:219px;top:41px;width:96px;height:127px" role="img" aria-label="Portrait photograph of the course author"></div>
  <ul class="s5list">
    <li>64 companies invested in</li>
    <li>35 companies have gotten to Series A</li>
    <li>$1.08B+ capital raised by my portfolio companies</li>
    <li>8 exits to date</li>
    <li>Consulting business working with early-stage founders across 5 continents</li>
    <li>90% margins</li>
  </ul>
  <div class="brand">LANTERN PEAK</div>
  <div class="num">5</div>
</section>

<section class="slide c3 r2">
  <h2 class="s6h">Why I Created This Course</h2>
  <div class="s6u"></div>
  <div class="blk" style="left:0;top:49px;width:8px;height:121px"></div>
  <div class="blk" style="left:357px;top:49px;width:8px;height:121px"></div>
  <div class="s6sub">Spent 6 years chatting with over 3,000 founders and learned:</div>
  <ul class="s6list">
    <li>The fundraising process is NOT transparent</li>
    <li>Founders don't know where to begin, who to talk to or where to start</li>
    <li>Founders don't get the candid feedback they need</li>
    <li>There is not easy way to find the right type of investors</li>
    <li>Founders don't always know what investors want, how to present it and the what the necessary KPI's for success are</li>
    <li>Founders underestimate how hard, long and tedious this process is start to finish</li>
    <li>The result is a fragmented, slow and challenging journey that leaves founders feeling empty and ultimately unfunded.</li>
  </ul>
  <div class="brand">LANTERN PEAK</div>
  <div class="num">6</div>
</section>

<!-- Row 3 -->
<section class="slide c1 r3">
  <div class="s7img dark-img" role="img" aria-label="Dark photograph of a glass office tower"></div>
  <div class="s7sq"></div>
  <h2 class="s7h">Expected<br>Results<br>For<br>Founders</h2>
  <ul class="s7list">
    <li>Founders now have a firm understanding of the fundraising process end-to-end</li>
    <li>Founder have resources to help them find the right investors at the right time</li>
    <li>Founders understand the different types of investors, motivation and stages</li>
    <li>Founders understand how to tell their story more effectively</li>
    <li>Founders feel equipped to successfully raise capital from the right type of investors</li>
    <li>Founders reduce to fundraise from 6-8 months to 3-6 mths</li>
  </ul>
  <div class="brand">LANTERN PEAK</div>
  <div class="num">7</div>
</section>

<section class="slide c2 r3">
  <div class="s8img dark-img" role="img" aria-label="Dark photograph of office buildings"></div>
  <h2 class="s8h">Who Is<br>This Course for?</h2>
  <div class="s8u"></div>
  <ul class="s8list">
    <li>Early-Stage founders considering raising outside capital to fund their company.</li>
    <li>Founders looking to understand the fundraising process along with the players involved</li>
    <li>Founders who are looking to accelerate the capital raising process for their company.</li>
    <li>Founders who are looking to nail their ICP (Ideal Customer Profile) for investors</li>
    <li>Founders who are frustrated with how long and hard the fundraising process can be.</li>
  </ul>
  <h2 class="s8h2">Who Isn't<br><b>This Course<br>For ?</b><span class="s8line"></span></h2>
  <ul class="s8list2">
    <li>Tire Kickers</li>
    <li>Wantrapreneurs vs Entrepreneurs</li>
    <li>Founders at Series A and beyond</li>
    <li>Founders who are not willing to do the work</li>
  </ul>
  <div class="brand">LANTERN PEAK</div>
  <div class="num">8</div>
</section>

<section class="slide c3 r3">
  <h2 class="s9h">The<span class="s9line"></span><br>Fundraising Journey</h2>
  <div class="vbar" style="left:38px;top:71px"><span>Two Years Ago (2022)</span></div>
  <ul class="s9list" style="left:60px;top:77px">
    <li>Founders could raise pre-revenue on just a deck</li>
    <li>Average number of investor conversations 100-150</li>
    <li>Average time to raise 3-6 months</li>
    <li>Pre-Seed Valuations $5M-15M</li>
    <li>LP's making decisions in 1-2 calls and FOMO</li>
  </ul>
  <div class="vbar" style="left:202px;top:71px"><span>Today</span></div>
  <ul class="s9list s9plain" style="left:226px;top:78px">
    <li>Founders need customers and revenue ($10K-25K MRR)</li>
    <li>Average number of investor conversations 200-300</li>
    <li>Average time to raise 5-8 months</li>
    <li>Pre-Seed Valuations $3M-10M</li>
    <li>LP's making decision in 4-6 calls</li>
  </ul>
  <div class="brand">LANTERN PEAK</div>
  <div class="num">9</div>
</section>

<!-- Row 4 -->
<section class="slide c1 r4">
  <h2 class="s10h">It's All<span class="s10line"></span><br>About The Story</h2>
  <div class="s10box"></div>
  <ul class="s10list">
    <li>This is your chance to share your vision</li>
    <li>Can you tell your story from the customers perspective</li>
    <li>Use simple words, not jargon</li>
    <li>Explain what you do so your "nana" could understand it</li>
    <li>Revenue solves everything</li>
  </ul>
  <ul class="s10list2">
    <li>Storytelling is a "full body" experience - Stand up, move around and point to screen</li>
    <li>Speak in numbers – Founders who build big companies are data driven
      <ul style="margin-left:6px"><li>Example: We grew 40% per month for the last 6 months and are now at $100K MRR.</li></ul>
    </li>
  </ul>
  <div class="brand">LANTERN PEAK</div>
  <div class="num">10</div>
</section>

<section class="slide c2 r4">
  <h2 class="s11h">Accelerators –<br>Good/Bad/Maybe</h2>
  <div class="vbar s11bar" style="left:36px;top:58px"><span style="transform:rotate(90deg)">Benefits of Accelerators</span></div>
  <ul class="s11list" style="left:59px;top:68px">
    <li>One-on-one mentoring with industry experts</li>
    <li>Access to alumni ecosystem of support</li>
    <li>Structured demo day to connect you with capital sources</li>
    <li>Provides credibility and signaling to investors</li>
    <li>Potential infusion of cash</li>
  </ul>
  <div class="vbar s11bar" style="left:201px;top:58px"><span style="transform:rotate(90deg)">Drawbacks of Accelerators</span></div>
  <ul class="s11list" style="left:224px;top:66px">
    <li>Low acceptance rate (under 2% on average)</li>
    <li>Big time commitment (12-16 weeks)</li>
    <li>Pressure to perform in a set period of time</li>
    <li>Cash can be expensive ($100K for 6%)</li>
    <li>LP's making decision in 4-6 calls</li>
  </ul>
  <div class="s11foot">Bottom Line<br>Accelerators are an advantage but NOT a necessity</div>
  <div class="brand">LANTERN PEAK</div>
  <div class="num">11</div>
</section>

<section class="slide c3 r4">
  <div class="s12img dark-img" role="img" aria-label="Dark photograph of a winding road through hills"></div>
  <h2 class="s12h">Why<br>Not Elm<br>Ridge<br>Road?</h2>
  <ul class="s12list">
    <li>Elm Ridge Rd has some of the most famous VC funds
      <ul><li>Redwood Arc Capital</li><li>Slatehill Partners</li><li>Marlow Ventures</li><li>Voltline Ventures</li><li>Ashford Kellerman</li></ul>
    </li>
    <li>Most rounds are too small for these funds ($100M-$1B in size)</li>
    <li>These funds are looking for 100X + ROI (aka Unicorns)</li>
    <li>Massive portfolios does NOT always mean massive help</li>
    <li>For early rounds, founders might be better off with other funding sources</li>
  </ul>
  <div class="brand">LANTERN PEAK</div>
  <div class="num">8</div>
</section>

</body>
</html>
```